T&R Custom Homes and Remodeling Flyer

We need a new double sided flyer that showcases our service.
Our website is http://trhomesbuildco.example/
Please use the information on http://trhomesbuildco.example/about-us/ for the information in the flyer.
This handout will be used to give to our potential customers and needs to show the complete story of who we are and the services we provide. I have also attached pictures of project we have completed that should be used for the flyer.
Any other pictures can be taken from our photo gallery on the website.

Target Market(s)

Clients who want a custom home or remodel

Industry/Entity Type

Construction

Font styles to use
Serif

Requirements
Must have
• Prominent logo
• Pictures of completed projects
• Tri-fold design- eps file is attached for this
Nice to have
• Manly colors
• If you can find a tasteful way to add the picture of the owners that is great, but it should be small and is not necessary.
Should not have
• Pink/girly touches

```html
<!DOCTYPE html>
<html lang="en">
<head>
<meta charset="utf-8">
<title>T&amp;R Custom Homes and Remodeling – Tri-fold Flyer</title>
<link rel="stylesheet" href="https://fonts.googleapis.com/css2?family=Roboto+Slab:wght@400;700&family=Merriweather:ital,wght@0,400;0,700;1,400&display=swap">
<style>
:root{
  --navy:#1f2d45;
  --teal:#2f6b66;
  --white:#ffffff;
  --ink:#2b2b2b;
  --page:#e6e7e9;
  --wood:linear-gradient(135deg,#6b3b22,#3d2416);
  --stone:linear-gradient(160deg,#c9c7c1,#8d8a84);
}
*{box-sizing:border-box;margin:0;padding:0}
html,body{width:1200px;height:1000px;overflow:hidden}
body{background:var(--page);font-family:"Merriweather",Georgia,serif;color:var(--ink);position:relative}
.spread{position:absolute;left:300px;width:600px;height:470px;background:var(--white);box-shadow:0 2px 8px rgba(0,0,0,.2);overflow:hidden}
.spread--outside{top:15px}
.spread--inside{top:510px}
.panel{position:absolute;top:0;width:200px;height:470px}
.abs{position:absolute}
.photo{position:absolute}
.label{position:absolute;background:var(--teal);color:var(--white);font-family:"Roboto Slab",Georgia,serif;font-weight:700;font-size:9px;letter-spacing:.3px;padding:5px 8px;text-transform:uppercase;line-height:1.25}
.label--navy{background:var(--navy)}
.copy{font-size:7.4px;line-height:1.38}
.copy strong{font-family:"Roboto Slab",Georgia,serif;font-weight:700;text-transform:uppercase;color:var(--teal)}
.on-dark{color:#d5dbe3}
.on-dark strong{color:var(--white)}
.brand{font-family:"Roboto Slab",Georgia,serif;font-weight:700;color:var(--navy);text-align:center;line-height:1.1}
.brand__mark{display:block;width:14px;height:14px;background:var(--navy);margin:0 auto 6px}
.brand--light{color:var(--white)}
.brand--light .brand__mark{background:var(--white)}
.contact{font-size:6.5px;color:#d5dbe3;text-align:center;line-height:1.6}
/* outside */
.cover{left:400px;background:var(--navy)}
.cover__bar{left:20px;top:0;width:160px;height:24px;background:var(--teal)}
.cover__logo{left:15px;top:28px;width:170px;height:125px;background:var(--white);padding-top:28px}
.cover__logo .brand{font-size:17px}
.cover__logo .brand small{display:block;font-size:8px;margin-top:3px;letter-spacing:.4px}
.cover__tagline{left:0;top:153px;width:200px;height:22px;background:var(--white);font-style:italic;font-size:9px;color:var(--teal);text-align:center;line-height:18px}
.cover__door{left:0;top:175px;width:200px;height:236px;background:linear-gradient(180deg,#d7d4cc 0%,#bdb8ae 35%,#5a2a1c 60%,#3e1d14 100%)}
.cover__phone{left:25px;top:410px;width:150px;height:24px;background:var(--white);font-family:"Roboto Slab",Georgia,serif;font-weight:700;font-size:13px;color:var(--navy);text-align:center;line-height:24px;letter-spacing:.5px}
.cover__web{left:0;top:441px;width:200px;font-family:"Roboto Slab",Georgia,serif;font-weight:700;font-size:9px;color:var(--white);text-align:center}
.story{left:200px;background:var(--navy)}
.story__block{left:10px;top:0;width:125px;height:240px;background:var(--teal)}
.story__text{left:16px;top:84px;width:120px}
.story__owners{left:88px;top:12px;width:82px;height:62px;background:var(--white);padding:3px}
.story__owners .photo{position:static;height:46px;width:100%;background:linear-gradient(180deg,#b9c2c8,#3a3f47)}
.story__owners p{font-size:5px;font-weight:700;text-align:center;margin-top:2px;color:var(--navy);white-space:nowrap}
.story__kitchen{left:0;top:228px;width:200px;height:150px;background:var(--wood)}
.story__label{left:80px;top:240px}
.story__footer{left:0;top:378px;width:200px;height:92px;padding-top:16px}
.story__footer .brand{font-size:10px;margin-bottom:8px}
.quality{left:0;background:var(--white)}
.quality__intro{right:12px;top:16px;width:150px;text-align:right}
.quality__label{left:12px;top:112px}
.quality__kitchen{left:12px;top:162px;width:188px;height:140px;background:linear-gradient(150deg,#4a3528,#8c6a4f 55%,#2e2621)}
.quality__body{left:12px;top:312px;width:178px}
.quality__badge{float:right;width:110px;margin:4px 0 4px 8px;background:var(--teal);color:var(--white);font-family:"Roboto Slab",Georgia,serif;font-weight:700;font-size:8.5px;line-height:1.25;text-align:center;text-transform:uppercase;padding:5px 6px;border:1px solid var(--white);outline:2px solid var(--teal)}
/* inside */
.deck{left:0;top:0;width:395px;height:245px;background:linear-gradient(180deg,#c9cdd2 0%,#a8a59d 45%,#4a3a30 75%,#6d6760 100%)}
.before{left:405px;top:25px;width:170px;height:130px;background:var(--stone)}
.after{left:405px;top:210px;width:170px;height:220px;background:linear-gradient(180deg,#8b5a44 0%,#b5a99a 45%,#c8c0b2 100%)}
.tag{position:absolute;background:var(--navy);color:var(--white);font-family:"Roboto Slab",Georgia,serif;font-size:6px;padding:3px 6px;letter-spacing:.5px}
.mission{left:200px;top:160px;width:392px;height:54px;background:var(--teal);color:var(--white);font-family:"Roboto Slab",Georgia,serif;font-weight:700;font-size:8.2px;text-align:center;line-height:1.4;padding-top:7px;text-transform:uppercase;z-index:2}
.chandelier{left:105px;top:195px;width:140px;height:140px;background:radial-gradient(circle at 55% 40%,#f3e9d8,#c9b89c 60%,#8d7c66);border:3px solid var(--white);z-index:1}
.craft__label{left:12px;top:255px;z-index:2}
.bath{left:10px;top:300px;width:160px;height:130px;background:linear-gradient(160deg,#2e2420,#6b5446 55%,#c7b9a6)}
.partners{left:252px;top:258px;width:141px;text-align:right}
.standards{left:210px;top:346px;width:185px}
</style>
</head>
<body>

<section class="spread spread--outside" aria-label="Outside of tri-fold">
  <div class="panel quality">
    <svg class="abs" style="left:0;top:0" width="200" height="160" aria-hidden="true">
      <polygon points="12,0 200,0 200,155 130,155 12,30" fill="var(--navy)"/>
    </svg>
    <p class="abs copy on-dark quality__intro">With more than 20 years combined experience in construction, <strong>T&amp;R maintains the absolute highest levels of quality, material, workmanship, and service in each and every project we build.</strong></p>
    <div class="label quality__label">Highest Quality</div>
    <div class="photo quality__kitchen" role="img" aria-label="Completed kitchen with dark cabinets and island bar"></div>
    <p class="abs copy quality__body">A reputation is only as great as the last referral and we understand that the future of our business relies upon satisfied customers. <strong>We take the time to fully understand our customer's expectations.</strong> Customer service is more <span class="quality__badge">100% Satisfaction Guaranteed</span>than just a trendy marketing theme, it is the underlying philosophy in everything we do and our home buyers reap the benefits of this philosophy.</p>
  </div>

  <div class="panel story">
    <div class="abs story__block"></div>
    <div class="abs story__owners">
      <div class="photo" role="img" aria-label="Small portrait of the two owners"></div>
      <p>Tom Reyes &amp; Rick Tallon</p>
    </div>
    <p class="abs copy on-dark story__text">Throughout our experience we have <strong>developed lasting values of honesty, real quality, attention to fine detail, efficiency, timeliness, and most of all how to meet a customers expectation by asking the right questions.</strong> With these principles, character and dedication we are able to do things right the first time.</p>
    <div class="photo story__kitchen" role="img" aria-label="Kitchen with wood cabinetry and granite counters"></div>
    <div class="label label--navy story__label">Fine Detail</div>
    <div class="abs story__footer">
      <div class="brand brand--light"><span class="brand__mark"></span>T&amp;R Custom Homes</div>
      <p class="contact">1200 Example Avenue Suite 102 - Springfield, IL 60000, USA<br>555-014-2290 | www.trhomesbuildco.example</p>
    </div>
  </div>

  <div class="panel cover">
    <div class="abs cover__bar"></div>
    <div class="abs cover__logo">
      <div class="brand"><span class="brand__mark"></span>T&amp;R CUSTOM HOMES<small>AND REMODELING</small></div>
    </div>
    <p class="abs cover__tagline">“Where every detail matters”</p>
    <div class="photo cover__door" role="img" aria-label="Arched entry with double wooden front doors and columns"></div>
    <p class="abs cover__phone">555-014-2290</p>
    <p class="abs cover__web">www.trhomesbuildco.example</p>
  </div>
</section>

<section class="spread spread--inside" aria-label="Inside of tri-fold">
  <div class="photo deck" role="img" aria-label="Rear of a custom home with large wooden deck"></div>
  <div class="photo before" role="img" aria-label="Front entry before remodel"></div>
  <span class="tag" style="left:408px;top:54px">BEFORE</span>
  <div class="photo after" role="img" aria-label="Front entry after remodel with stone columns"></div>
  <span class="tag" style="left:540px;top:272px">AFTER</span>
  <p class="abs mission">T&amp;R is committed to building quality homes<br>with meticulous craftsmanship, custom designs,<br>and thoughtful touches that add<br>to the homeowners' quality of life.</p>
  <div class="photo chandelier" role="img" aria-label="Wrought iron chandelier in a finished room"></div>
  <div class="label label--navy craft__label">Highest Level<br>of Craftsmanship</div>
  <div class="photo bath" role="img" aria-label="Bathroom vanity with dark cabinets and mirror"></div>
  <p class="abs copy partners">Over the years, we have developed close working relationships with some of the best local craftsmen, vendors, and suppliers located in the western suburbs of Chicago.</p>
  <p class="abs copy standards">These trade partners know <strong>we expect only the highest level of craftsmanship and they are required to perform at only the highest standards of professionalism, accuracy and timeliness.</strong> We take pride in creating homes that are as beautiful to look at, as they are comfortable to live in.</p>
</section>

</body>
</html>
```